Beauty Salon Treatment Menu & Pricing

We need a Treatment Pricelist/ Brochure made to hand out to potential & existing customers! Meadowlark Body & Makeup is a small friendly beauty salon focused on the beauty essentials such as waxing, spray tanning, facials & makeup. We have a webpage with our colour theme and style and we would like to brochure to tie in.
www.meadowlarkbodyandmakeup.com.au.
We like a brochure that is clean, simple and easy to read.

Industry/Entity Type

Beauty Salon

```html
<!DOCTYPE html>
<html lang="en">
<head>
<meta charset="utf-8">
<title>Meadowlark Body &amp; Makeup – Treatment Brochure</title>
<link rel="stylesheet" href="https://fonts.googleapis.com/css2?family=Raleway:wght@200;300;400&family=Open+Sans:wght@400;600&display=swap">
<style>
  :root {
    --red: #e03c44;
    --red-deep: #c8313a;
    --red-soft: #ee7c80;
    --white: #ffffff;
    --backdrop: #efe9e2;
    --photo-light: #c9c9c9;
    --photo-dark: #6f6f6f;
    --tile-dark: #3b3234;
  }
  * { box-sizing: border-box; margin: 0; padding: 0; }
  html, body { width: 1200px; height: 1024px; overflow: hidden; }
  body {
    background: var(--backdrop);
    font-family: "Open Sans", Arial, sans-serif;
    color: var(--white);
    position: relative;
  }
  .panel {
    position: absolute;
    top: 70px;
    width: 370px;
    height: 884px;
    background: var(--red);
    box-shadow: 0 6px 18px rgba(0,0,0,.18);
    overflow: hidden;
  }
  .panel--cover { left: 30px; }
  .panel--about { left: 415px; }
  .panel--services { left: 800px; }

  /* Brand name */
  .brand { text-align: center; font-family: "Raleway", Arial, sans-serif; font-weight: 300; }
  .brand__name { font-size: 40px; letter-spacing: 3px; line-height: 1; }
  .brand__sub { font-size: 15px; letter-spacing: 4px; margin-top: 8px; }

  /* Cover */
  .panel--cover .brand { margin-top: 110px; }
  .photo-band {
    position: absolute; left: 0; right: 0;
    border-top: 8px solid var(--red-soft);
    border-bottom: 8px solid var(--red-soft);
  }
  .photo-band .photo { width: 100%; height: 100%; }
  .cover__band { top: 250px; height: 250px; }
  .cover__band .photo { background: linear-gradient(135deg, var(--photo-light), #9a9a9a 60%, var(--photo-dark)); }
  .cover__tagline {
    position: absolute; top: 530px; right: 24px; left: 16px;
    text-align: right; white-space: nowrap;
    font-family: "Raleway", Arial, sans-serif; font-weight: 200;
    font-size: 32px; line-height: 1.2;
  }
  .cover__phone {
    position: absolute; top: 672px; right: 24px;
    font-family: "Raleway", Arial, sans-serif; font-weight: 200;
    font-size: 40px; line-height: 1; letter-spacing: 1px;
    white-space: nowrap;
  }
  .hours {
    position: absolute; right: 0; bottom: 36px; width: 190px;
    background: var(--red-deep); padding: 10px 14px;
    font-size: 9.5px; line-height: 1.5;
  }
  .hours__title { font-weight: 600; font-size: 12px; margin-bottom: 3px; }
  .cover__web {
    position: absolute; left: 0; right: 0; bottom: 0; height: 36px;
    background: var(--red-deep); border-top: 2px solid var(--red-soft);
    font-size: 12px; text-align: center; line-height: 34px;
  }

  /* About */
  .panel--about .brand { margin-top: 40px; }
  .panel--about .brand__name { font-size: 34px; }
  .panel--about .brand__sub { font-size: 12px; }
  .about__body { padding: 30px 26px 0; font-size: 10.5px; line-height: 1.55; text-align: justify; }
  .about__body p { margin-bottom: 14px; }
  .price-list { margin: 14px 26px 0; font-size: 10.5px; }
  .price-list__title { font-family: "Raleway", Arial, sans-serif; font-size: 16px; font-weight: 400; margin-bottom: 6px; }
  .price-list__row { display: flex; justify-content: space-between; padding: 3px 0; border-bottom: 1px solid var(--red-soft); }

  /* Services */
  .service-tabs { display: flex; justify-content: center; gap: 8px; margin-top: 54px; }
  .service-tab {
    width: 56px; height: 42px; border-radius: 3px;
    background: linear-gradient(160deg, #8a7c7e, var(--tile-dark));
    box-shadow: 0 1px 3px rgba(0,0,0,.35);
    display: flex; align-items: center; justify-content: center;
    font-size: 10px; letter-spacing: .5px;
  }
  .services__band { top: 140px; height: 210px; }
  .services__band .photo { background: linear-gradient(120deg, #8a8a8a, var(--photo-light) 45%, #e5e5e5); }
  .services__body { position: absolute; top: 380px; left: 26px; right: 26px; font-size: 10.5px; line-height: 1.5; text-align: justify; }
  .gallery {
    position: absolute; top: 530px; left: 50px; width: 270px;
    display: grid; grid-template-columns: repeat(8, 1fr); gap: 3px;
  }
  .gallery span { aspect-ratio: 1; background: linear-gradient(135deg, #b9a9a6, #6d5f60); }
</style>
</head>
<body>

<section class="panel panel--cover">
  <div class="brand">
    <div class="brand__name">MEADOWLARK</div>
    <div class="brand__sub">BODY &amp; MAKEUP</div>
  </div>
  <div class="photo-band cover__band">
    <div class="photo" role="img" aria-label="Black and white photo of a makeup artist preparing a bride"></div>
  </div>
  <h1 class="cover__tagline">Everything you need<br>at the one beauty<br>appointment</h1>
  <div class="cover__phone">0400 123 456</div>
  <div class="hours">
    <div class="hours__title">Opening Hours:</div>
    Tue - Wed 9:00 am - 5:00 pm<br>
    Thu 11:00 am - 8:00 pm<br>
    Fri 9:00 am - 5:00 pm<br>
    Sat 8:00 am - 3:00 pm
  </div>
  <div class="cover__web">www.meadowlarkbodyandmakeup.com.au</div>
</section>

<section class="panel panel--about">
  <div class="brand">
    <div class="brand__name">MEADOWLARK</div>
    <div class="brand__sub">BODY &amp; MAKEUP</div>
  </div>
  <div class="about__body">
    <p>Here at Meadowlark Body &amp; Makeup we strive to make sure you leave your appointment with expectations exceeded. We offer a relaxed professional salon environment with a high percentage of repeat customers. We tailor our services to the individual, ensuring our clients leave happy and satisfied!</p>
    <p>Owner Tessa is a bubbly and energetic therapist with a passion to enhance your natural beauty image! Over the years Tessa worked mainly in a day spa setting, including her work on the Coral Star cruise liner as a therapist. Once back in Perth she went on to work for a leading brand where she developed more of a flare and passion for makeup, and understanding the importance of skincare she went on to opening Meadowlark Body and Makeup. With Tessa's knowledge you can be sure of a professional and friendly service.</p>
    <p>Qualified beauty therapist Nina holds valuable experience and specialises in all areas of waxing, tanning and peels. With Nina's extensive training as well as care, you can expect your treatment to be a pleasant one.</p>
  </div>
  <div class="price-list">
    <div class="price-list__title">Waxing</div>
    <div class="price-list__row"><span>Lip</span><span>$12.00</span></div>
    <div class="price-list__row"><span>Chin</span><span>$12.00</span></div>
    <div class="price-list__row"><span>Stomach</span><span>$15.00</span></div>
    <div class="price-list__row"><span>Back</span><span>$35.00</span></div>
    <div class="price-list__row"><span>Patches</span><span>$10.00</span></div>
  </div>
</section>

<section class="panel panel--services">
  <nav class="service-tabs">
    <div class="service-tab">NAILS</div>
    <div class="service-tab">MAKE-UP</div>
    <div class="service-tab">WAX</div>
    <div class="service-tab">SKIN</div>
    <div class="service-tab">TAN</div>
  </nav>
  <div class="photo-band services__band">
    <div class="photo" role="img" aria-label="Black and white close-up of eyeliner being applied"></div>
  </div>
  <div class="services__body">
    <p>Meadowlark Body &amp; Makeup offers everything you need at the one beauty appointment.</p>
    <p>Our staff are fully qualified professionals specialising in waxing, eyebrows, makeup, spray tanning and facial peel treatments.</p>
    <p>Only the highest quality products are used with the strictest level of health and hygiene maintained.</p>
  </div>
  <div class="gallery" role="img" aria-label="Grid of small photos of makeup looks, nails and salon clients">
    <span></span><span></span><span></span><span></span><span></span><span></span><span></span><span></span>
    <span></span><span></span><span></span><span></span><span></span><span></span><span></span><span></span>
    <span></span><span></span><span></span><span></span><span></span><span></span><span></span><span></span>
    <span></span><span></span><span></span><span></span><span></span><span></span><span></span><span></span>
    <span></span><span></span><span></span>
  </div>
</section>

</body>
</html>
```